Real Estate Entrepreneur needs a business card

I am a real estate entrepreneur, I buy houses for investment purposes, I act as a real estate agent representing buyers and sellers in residential home transactions, I am a contractor that does a wide range of home repairs and construction. I'd like a design that can stick with me through the years as my business grows and morphs to fit any niche I decide to pursue as markets change.

Target Market(s)

Anyone with interest that may be related to real estate.

Industry/Entity Type

Real Estate

Contact Information for Business Card

A card that stands out and doesn't put me in any one box. My business will evolve over time and I need a card that can stay relevant.

Colors

Designer to choose colors to be used in the design.

Requirements
Must have
• Character
Nice to have
• I'm open
Should not have
• Cliche houses and hammers

```html
<!DOCTYPE html>
<html lang="en">
<head>
<meta charset="UTF-8">
<title>Daniel Moreau – Real Estate Business Card</title>
<link href="https://fonts.googleapis.com/css2?family=Marcellus+SC&family=Montserrat:wght@300;400&display=swap" rel="stylesheet">
<style>
  :root {
    --stage: #0d1117;
    --card-top: #3a4654;
    --card-bottom: #1b222b;
    --card-front-top: #27313c;
    --card-front-bottom: #141a21;
    --ink-light: #e4e8ec;
    --ink-soft: #b7c0c9;
    --accent: #1a8fd6;
    --accent-deep: #137bbd;
    --silver: #b9bab6;
  }
  * { margin: 0; padding: 0; box-sizing: border-box; }
  html, body {
    width: 1200px; height: 786px; overflow: hidden;
    background: var(--stage);
  }
  .canvas {
    width: 1200px; height: 786px;
    display: flex; align-items: center; justify-content: center; gap: 60px;
  }
  .card {
    position: relative;
    width: 500px; height: 286px;
    border-radius: 16px;
    overflow: hidden;
    box-shadow: 0 14px 40px rgba(0,0,0,.55);
  }
  /* Back: name centred */
  .card--back {
    background: linear-gradient(160deg, var(--card-top), var(--card-bottom));
    display: flex; flex-direction: column; align-items: center; justify-content: center;
  }
  .card__name {
    font-family: "Marcellus SC", serif;
    font-weight: 400;
    letter-spacing: 2px;
  }
  .card--back .card__name {
    color: var(--ink-light);
    font-size: 44px;
  }
  .card--back .card__field {
    font-family: "Montserrat", sans-serif;
    font-weight: 300;
    color: var(--ink-soft);
    font-size: 15px;
    letter-spacing: 1.5px;
    margin-top: 2px;
  }
  /* Front: details */
  .card--front {
    background: linear-gradient(150deg, var(--card-front-top), var(--card-front-bottom));
  }
  .card--front .card__name {
    position: absolute; left: 38px; top: 42px;
    color: var(--accent);
    font-size: 30px;
  }
  .card__role {
    position: absolute; left: 38px; top: 78px;
    font-family: "Montserrat", sans-serif; font-weight: 300;
    color: var(--ink-soft); font-size: 12px; letter-spacing: .5px;
  }
  .contact {
    position: absolute; right: 34px; top: 148px;
    list-style: none;
    font-family: "Montserrat", sans-serif; font-weight: 400;
    color: var(--ink-light); font-size: 13px;
  }
  .contact__item { display: flex; align-items: center; gap: 9px; margin-bottom: 9px; }
  .contact__icon { width: 17px; height: 17px; flex: none; }
  .edge-strip {
    position: absolute; left: 0; bottom: 0;
    width: 230px; height: 8px;
    background: var(--silver);
  }
  .tab {
    position: absolute; right: 0; bottom: 0;
    width: 280px; height: 56px;
    background: linear-gradient(180deg, var(--accent), var(--accent-deep));
    border-top-left-radius: 36px;
    display: flex; align-items: center; justify-content: center;
    font-family: "Montserrat", sans-serif; font-weight: 400;
    color: var(--ink-light); font-size: 17px; letter-spacing: 1px;
  }
</style>
</head>
<body>
  <main class="canvas">
    <section class="card card--front">
      <h1 class="card__name">Daniel Moreau</h1>
      <p class="card__role">Agent</p>
      <ul class="contact">
        <li class="contact__item">
          <svg class="contact__icon" viewBox="0 0 20 20" aria-hidden="true">
            <circle cx="10" cy="10" r="10" fill="var(--accent)"/>
            <path d="M7 5.5c.6 0 1.2 1.6 1.3 2.1.1.5-.8 1-.7 1.4.4 1.2 1.3 2.1 2.4 2.6.4.1.9-.8 1.4-.7.5.1 2.1.7 2.1 1.3 0 .9-1 1.8-2 1.6C8.4 13.3 6.6 11.5 5.9 8.5c-.2-1 .3-3 1.1-3z" fill="#141a21"/>
          </svg>
          <span>+41 61 555 07 48</span>
        </li>
        <li class="contact__item">
          <svg class="contact__icon" viewBox="0 0 20 20" aria-hidden="true">
            <circle cx="10" cy="10" r="10" fill="var(--accent)"/>
            <rect x="5" y="6.5" width="10" height="7" rx="1" fill="#141a21"/>
            <path d="M5.5 7.2 10 10.5l4.5-3.3" stroke="var(--accent)" stroke-width="1" fill="none"/>
          </svg>
          <span>daniel.m@keyhollow.com</span>
        </li>
      </ul>
      <div class="edge-strip"></div>
      <div class="tab">Real Estate</div>
    </section>

    <section class="card card--back">
      <h2 class="card__name">Daniel Moreau</h2>
      <p class="card__field">Real Estate</p>
    </section>
  </main>
</body>
</html>
```